tourism marketplace web app redesign*

Hi, I need our front-page redesigned. For the competition please submit a jpg of ABOVE THE FOLD ONLY. The full page redesign will be a revision request. URL is https://qp.trolvexa.hu/hu/index.html login:'fullhd' and password:'asdasd' (Fold is supposed to be at "Kiemelt Ajanlatok", use all elements above that. Please use at least one extra color other than the two in the logo, or you may completely change them. FOCUS should be on the central combined search box (3 dropdown, 2 calendar picker + Kereses Button) just like nestorly.com, ravimoto.com, Pelusi.com, etc... The search box is always large, central, white, we want that too. We want it to look more modern, more clean AND we want to feature a changing beautiful nature photo background (like nestorly.com).Please use our newly designed logo (in attached pdf) and use that new spelling: "ferntrail.online"

```html
<!DOCTYPE html>
<html lang="hu">
<head>
<meta charset="utf-8">
<title>ferntrail.online – Vadászat közvetlenül</title>
<link rel="stylesheet" href="https://fonts.googleapis.com/css2?family=Ubuntu:wght@400;500;700&family=Montserrat:wght@700;800&family=Open+Sans:wght@400;600&display=swap">
<style>
  :root{
    --bar-brown:#463a2a;
    --btn-brown:#3a2e16;
    --ink:#2d2a26;
    --white:#ffffff;
    --teal:#5eab97;
    --green:#21c91f;
    --green-dark:#1aa819;
    --field-text:#6f6f6f;
    --divider:#e3e3e3;
  }
  *{box-sizing:border-box;margin:0;padding:0}
  html,body{width:1200px;height:747px;overflow:hidden;background:var(--white)}
  body{position:relative;font-family:"Ubuntu",sans-serif;color:var(--ink)}

  .topbar{position:absolute;left:0;top:0;width:1200px;height:29px;background:var(--bar-brown);
    font-family:"Open Sans",sans-serif;font-size:11px;color:var(--white)}
  .topbar span{position:absolute;top:7px;white-space:nowrap}
  .topbar .size{left:766px;color:#2a2218}
  .topbar .lang{left:799px}
  .topbar .cur{left:859px}
  .topbar .caret{display:inline-block;margin-left:7px;border:4px solid transparent;border-top:5px solid var(--white);vertical-align:-1px}
  .topbar .divider{position:absolute;top:0;width:1px;height:29px;background:#6a5c48}
  .topbar .account{left:910px;font-size:10px;color:#e6dcc8}

  .header{position:absolute;left:0;top:29px;width:1200px;height:85px;background:var(--white)}
  .brand{position:absolute;left:144px;top:16px;display:flex;align-items:center;gap:12px}
  .brand-dot{width:56px;height:56px;border-radius:50%;background:var(--teal)}
  .brand-name{font-weight:500;font-size:25px;color:#3d3d3d;white-space:nowrap}
  .nav{position:absolute;left:588px;top:37px;display:flex;gap:15px;font-size:12px;font-weight:500;color:#2f2f2f;white-space:nowrap}
  .partner-btn{position:absolute;left:928px;top:31px;width:128px;height:27px;background:var(--btn-brown);
    border-radius:2px;color:var(--white);font-size:12px;font-weight:700;display:flex;align-items:center;justify-content:center;gap:4px;white-space:nowrap}

  .hero{position:absolute;left:0;top:114px;width:1200px;height:633px;overflow:hidden}
  .hero-photo{position:absolute;inset:0;
    background:linear-gradient(180deg,#4f8ec6 0%,#7eb0d8 12%,#a9c4d6 20%,#3e5a3c 30%,#2f4a2e 40%,#7e8a84 50%,#9a9a84 56%,#b08a3c 66%,#a8752a 80%,#7d5620 100%)}
  .headline{position:absolute;left:0;top:108px;width:1200px;text-align:center;font-family:"Montserrat",sans-serif;
    font-weight:800;font-size:38px;line-height:49px;letter-spacing:3px;color:var(--white);text-shadow:0 2px 6px rgba(0,0,0,.35)}
  .tagline{position:absolute;left:0;top:218px;width:1200px;text-align:center;font-family:"Montserrat",sans-serif;
    font-weight:700;font-size:19px;letter-spacing:1.5px;color:var(--white);text-shadow:0 2px 4px rgba(0,0,0,.4)}

  .category{position:absolute;top:278px;width:240px;text-align:center}
  .category .ring{width:108px;height:108px;margin:0 auto;border-radius:50%;border:2px solid rgba(94,171,151,.85);
    display:flex;align-items:center;justify-content:center}
  .category .disc{width:96px;height:96px;border-radius:50%;background:var(--teal);display:flex;align-items:center;justify-content:center}
  .category.active .ring{border-color:var(--green)}
  .category.active .disc{background:var(--green)}
  .category .label{margin-top:21px;font-weight:700;font-size:21px;letter-spacing:-.4px;color:var(--white);
    text-shadow:0 2px 4px rgba(0,0,0,.45);white-space:nowrap}
  .cat-individual{left:226px}
  .cat-group{left:466px}
  .cat-packages{left:718px}

  .search{position:absolute;left:120px;top:456px;width:960px;height:74px;display:flex;align-items:center;
    background:var(--white);border-radius:14px;padding:8px;box-shadow:0 14px 36px rgba(0,0,0,.32)}
  .field{flex:1;height:58px;display:flex;align-items:center;justify-content:space-between;
    padding:0 20px;font-size:16px;color:var(--field-text);white-space:nowrap;border-right:1px solid var(--divider)}
  .field:nth-child(4){border-right:0}
  .field-date{flex:1.15}
  .field .icon{display:flex;align-items:center;gap:12px}
  .field .arrow{width:8px;height:8px;border-right:2px solid #666;border-bottom:2px solid #666;transform:rotate(45deg);margin-top:-4px}
  .search-btn{width:150px;height:58px;border-radius:10px;background:var(--green);color:var(--white);font-size:19px;font-weight:700;
    display:flex;align-items:center;justify-content:center;gap:8px;letter-spacing:.5px}
</style>
</head>
<body>

<div class="topbar">
  <span class="size">Large</span>
  <span class="lang">Magyar<i class="caret"></i></span>
  <span class="cur">EUR<i class="caret"></i></span>
  <i class="divider" style="left:902px"></i>
  <span class="account">&#9679; Regisztráció / Bejelentkezés</span>
  <i class="divider" style="left:1060px"></i>
</div>

<header class="header">
  <div class="brand"><span class="brand-dot"></span><span class="brand-name">ferntrail.online</span></div>
  <nav class="nav">
    <span>Országok</span><span>Vadfajok</span><span>Rólunk</span><span>ÁSZF</span><span>Hogyan működik</span>
  </nav>
  <div class="partner-btn">
    <svg width="10" height="10" viewBox="0 0 10 10"><circle cx="5" cy="5" r="5" fill="#fff"/><path d="M5 2.5v5M2.5 5h5" stroke="#3a2e16" stroke-width="1.6"/></svg>
    Legyen partnerünk
  </div>
</header>

<section class="hero">
  <div class="hero-photo" role="img" aria-label="Nature photo: snowy mountains, pine forest, a lake and golden autumn meadow with a bull elk on the right"></div>

  <h1 class="headline">YOU DON'T NEED A HUNTING<br>ORGANIZER!</h1>
  <p class="tagline">Foglalj közvetlen a vadászterületnél</p>

  <div class="category cat-individual">
    <div class="ring"><div class="disc">
      <svg width="50" height="54" viewBox="0 0 50 54" fill="#fff"><circle cx="25" cy="14" r="13"/><path d="M3 54c0-14 9-24 22-24s22 10 22 24z"/></svg>
    </div></div>
    <div class="label">Individual hunts</div>
  </div>

  <div class="category cat-group active">
    <div class="ring"><div class="disc">
      <svg width="58" height="44" viewBox="0 0 58 44" fill="#fff">
        <circle cx="12" cy="10" r="7"/><circle cx="46" cy="10" r="7"/><circle cx="29" cy="14" r="10"/>
        <path d="M0 34c0-8 5-13 12-13s9 3 9 3l-5 10z"/><path d="M58 34c0-8-5-13-12-13s-9 3-9 3l5 10z"/>
        <path d="M11 44c0-11 8-18 18-18s18 7 18 18z"/>
      </svg>
    </div></div>
    <div class="label">Group hunts, Shoots</div>
  </div>

  <div class="category cat-packages">
    <div class="ring"><div class="disc">
      <svg width="60" height="60" viewBox="0 0 60 60" fill="none" stroke="#fff" stroke-width="2.5">
        <circle cx="28" cy="22" r="10"/>
        <path d="M28 15v14M31.5 18.5c-1-1.5-7-2-7 1s7 2 7 5-6 3-7 1" stroke-width="2"/>
        <path d="M24 4v5M29 2v7M34 5v4"/>
        <path d="M6 40l10-6 14 4-4 4-10-1M14 46l12 3 16-8v-4"/>
        <path d="M44 32v18M44 50h8"/>
      </svg>
    </div></div>
    <div class="label">Exclusive Packages</div>
  </div>

  <form class="search">
    <div class="field field-wild">All wild<i class="arrow"></i></div>
    <div class="field field-country">All countries<i class="arrow"></i></div>
    <div class="field field-offer">All offers<i class="arrow"></i></div>
    <div class="field field-date">Check In &nbsp;- Check Out
      <svg width="16" height="16" viewBox="0 0 14 14" fill="none" stroke="#666" stroke-width="1.2"><rect x="1" y="2" width="12" height="11" rx="1"/><path d="M1 5h12M4 0v3M10 0v3M4 7.5h1M7 7.5h1M10 7.5h1M4 10h1M7 10h1M10 10h1"/></svg>
    </div>
    <div class="search-btn">
      <svg width="18" height="18" viewBox="0 0 18 18" fill="none" stroke="#fff" stroke-width="2.4"><circle cx="7.5" cy="7.5" r="5.5"/><path d="M11.5 11.5l5 5"/></svg>
      SEARCH
    </div>
  </form>
</section>

</body>
</html>
```